Business Cards

Business cards (double-sided) to be handed out to clients and potential clients, with contact details, logo .

Target Market(s)

Small to medium size businesses

Industry/Entity Type

Accountants

Contact Information for Business Card

Brightmere Ledger Accounting & Advisory Ltd

Colors

Designer to choose only greyscale colors for use in the design.

Requirements
Must have
• Name, Title, Address, Phone number, Email, Website
Nice to have
• Modern, clean lines, classy
Should not have
• Business cards to be double-sided. Form keeps reverting to single-sided.

```html
<!DOCTYPE html>
<html lang="en">
<head>
<meta charset="utf-8">
<title>Brightmere Ledger – Business Cards</title>
<link href="https://fonts.googleapis.com/css2?family=Montserrat:wght@400;500;800&display=swap" rel="stylesheet">
<style>
  :root {
    --page: #d9d9d9;
    --card-white: #ffffff;
    --card-black: #141414;
    --ink: #111111;
    --band-dark: #2b2b2b;
    --band-grey: #8a8a8a;
    --reverse-ink: #f2f2f2;
  }
  * { box-sizing: border-box; margin: 0; padding: 0; }
  html, body { width: 1200px; height: 900px; overflow: hidden; }
  body {
    background: var(--page);
    font-family: "Montserrat", Arial, sans-serif;
    color: var(--ink);
    display: flex;
    flex-direction: column;
    align-items: center;
    justify-content: center;
    gap: 40px;
  }
  .card {
    position: relative;
    width: 700px;
    height: 400px;
    border-radius: 26px;
    overflow: hidden;
    box-shadow: 0 10px 30px rgba(0,0,0,.18);
  }
  .card--front { background: var(--card-white); }
  .card--back {
    background: var(--card-black);
    display: flex;
    align-items: center;
    justify-content: center;
  }

  .wordmark { font-weight: 500; text-transform: uppercase; }
  .wordmark__main { display: block; letter-spacing: .12em; }
  .wordmark__sub { display: block; letter-spacing: .22em; }

  .card--front .wordmark { position: absolute; left: 44px; top: 40px; }
  .card--front .wordmark__main { font-size: 24px; }
  .card--front .wordmark__sub { font-size: 9px; margin-top: 8px; }

  .card--back .wordmark { color: var(--reverse-ink); text-align: center; }
  .card--back .wordmark__main { font-size: 40px; }
  .card--back .wordmark__sub { font-size: 13px; margin-top: 14px; }

  .contact-list {
    position: absolute;
    left: 44px;
    top: 180px;
    list-style: none;
    font-size: 17px;
    line-height: 1;
  }
  .contact-list li { display: flex; align-items: center; gap: 12px; margin-bottom: 14px; }
  .contact-list svg { width: 16px; height: 16px; fill: var(--ink); flex: none; }

  .holder { position: absolute; right: 44px; top: 170px; text-align: right; }
  .holder__name { font-weight: 800; font-size: 22px; letter-spacing: .01em; text-transform: uppercase; }
  .holder__title { font-size: 16px; margin-top: 6px; }

  .address { position: absolute; right: 44px; bottom: 48px; text-align: right; font-size: 17px; line-height: 1.4; }

  .edge-band { position: absolute; left: 0; bottom: 0; width: 700px; height: 40px; }
</style>
</head>
<body>

  <section class="card card--front" aria-label="Business card front">
    <div class="wordmark">
      <span class="wordmark__main">Brightmere Ledger</span>
      <span class="wordmark__sub">Accounting &amp; Advisory Ltd</span>
    </div>

    <ul class="contact-list">
      <li>
        <svg viewBox="0 0 16 16" aria-hidden="true"><path d="M3.6 1.2l2.3 2.6-1.3 1.8c.9 2 2.6 3.7 4.6 4.6l1.8-1.3 2.6 2.3-1.4 2.5C6.5 13.6 2.4 9.5 1.2 3.8z"/></svg>
        555-210-4836
      </li>
      <li>
        <svg viewBox="0 0 16 16" aria-hidden="true"><path d="M1 3h14v10H1zM2.4 4.2L8 8.6l5.6-4.4z" fill-rule="evenodd"/></svg>
        hello@brightmereledger.com
      </li>
      <li>
        <svg viewBox="0 0 16 16" aria-hidden="true"><circle cx="8" cy="8" r="7"/><path d="M1 8h14M8 1c2.5 2.5 2.5 11.5 0 14M8 1c-2.5 2.5-2.5 11.5 0 14" stroke="#fff" stroke-width="1" fill="none"/></svg>
        www.brightmereledger.com
      </li>
    </ul>

    <div class="holder">
      <p class="holder__name">Dorian Wexley</p>
      <p class="holder__title">Co-Founder</p>
    </div>

    <p class="address">42 Alder Row 9<br>Fenwick, NY 10284</p>

    <svg class="edge-band" viewBox="0 0 700 40" preserveAspectRatio="none" aria-hidden="true">
      <polygon points="0,18 400,18 410,28 0,28" fill="var(--band-grey)"/>
      <polygon points="0,28 410,28 420,12 470,8 470,40 0,40" fill="var(--band-dark)"/>
    </svg>
  </section>

  <section class="card card--back" aria-label="Business card back">
    <div class="wordmark">
      <span class="wordmark__main">Brightmere Ledger</span>
      <span class="wordmark__sub">Accounting &amp; Advisory Ltd</span>
    </div>
  </section>

</body>
</html>
```